Clean Vormix Ads Banner Design For A Finance Company

Hi,
We're a UK based finance company and are looking for new banner ads to use on the Vormix Display Network.
We want the end product to stand out by using strong, minimal design - ideally starting from a dark theme, although I'm open to ideas.
The copy should read:
'Fast Bridging Loans From 0.39% PM'
Once we have these designs agreed, we are looking to replicate them for other products, changing only the text on each ad - for example, 'commercial mortgage service you can rely on' or 'development finance service you can rely on'.
The colours used on our website are the following:
Black - #040303
Orange - #f79124
White - #ffffff
Grey - #ffffff
Example ads that I like - https://www.plexabyte.com/wp-content/uploads/2021/07/vormix-display-ads-example-2-final.png.webp
2 - https://adquilterhub.com/wp-content/uploads/2020/03/fbdd56ba3bd16c7a8debb13a411de786.jpg

```html
<!DOCTYPE html>
<html lang="en">
<head>
<meta charset="UTF-8">
<title>Norvale Finance Limited – Bridging Loan Banner</title>
<link rel="stylesheet" href="https://fonts.googleapis.com/css2?family=Exo+2:wght@500;700&family=Russo+One&display=swap">
<style>
  :root {
    --ink: #040303;
    --orange: #f07a22;
    --orange-light: #ffc27a;
    --orange-deep: #d9601a;
    --white: #ffffff;
    --night: #0a1322;
    --night-2: #141d33;
    --bubble: #e9eef8;
    --bubble-shade: #c9d3e8;
    --icon: #3a4687;
    --suit: #2b4e8f;
    --suit-dark: #1a3366;
  }
  * { margin: 0; padding: 0; box-sizing: border-box; }
  html, body { width: 1200px; height: 2400px; overflow: hidden; background: var(--night); }
  .banner {
    position: relative;
    width: 1200px;
    height: 2400px;
    overflow: hidden;
    font-family: "Exo 2", sans-serif;
    color: var(--white);
  }
  .market-backdrop {
    position: absolute; inset: 0;
    background:
      radial-gradient(ellipse 420px 700px at 1080px 1150px, rgba(40,160,140,0.28), transparent 70%),
      radial-gradient(ellipse 360px 600px at 1000px 700px, rgba(150,60,150,0.25), transparent 70%),
      radial-gradient(ellipse 300px 700px at 120px 1500px, rgba(190,60,50,0.22), transparent 70%),
      radial-gradient(ellipse 500px 400px at 200px 500px, rgba(60,90,150,0.25), transparent 70%),
      linear-gradient(180deg, #0c1424 0%, var(--night-2) 45%, #0b1220 100%);
  }
  .brand {
    position: absolute; top: 180px; left: 0; width: 100%;
    text-align: center; color: var(--orange);
    font-family: "Exo 2", sans-serif; font-weight: 700;
  }
  .brand-name { display: block; font-size: 128px; line-height: 1; letter-spacing: -2px; }
  .brand-sub { display: block; font-size: 38px; line-height: 1.2; margin-top: 8px; }
  .headline {
    position: absolute; left: 80px; top: 540px; width: 1040px; height: 220px;
  }
  .headline text { font-family: "Russo One", sans-serif; }
  .tagline {
    position: absolute; top: 745px; left: 0; width: 100%;
    text-align: center; font-weight: 500; font-size: 74px; line-height: 88px;
    letter-spacing: 1px;
  }
  .chat-bubble { position: absolute; }
  .chat-bubble--bars { left: 120px; top: 1205px; width: 350px; height: 200px; }
  .chat-bubble--trend { left: 780px; top: 1195px; width: 265px; height: 180px; }
  .advisor-figure {
    position: absolute; left: 385px; top: 1200px; width: 540px; height: 840px;
    border-radius: 240px 240px 40px 40px;
    background: linear-gradient(180deg, #3a4a66 0%, var(--suit) 38%, var(--suit-dark) 100%);
  }
  .offer-panel { position: absolute; left: 0; top: 1940px; width: 1200px; height: 460px; }
  .offer-text {
    position: absolute; top: 2195px; left: 0; width: 100%;
    text-align: center; color: var(--ink);
    font-weight: 500; font-size: 64px; line-height: 70px;
  }
</style>
</head>
<body>
<main class="banner">
  <div class="market-backdrop" role="img" aria-label="Dark blurred stock market candlestick chart backdrop"></div>

  <div class="brand">
    <span class="brand-name">norvale</span>
    <span class="brand-sub">Finance Limited</span>
  </div>

  <svg class="headline" viewBox="0 0 1040 220" aria-label="Bridging">
    <defs>
      <linearGradient id="headline-fill" x1="0" y1="0" x2="0" y2="1">
        <stop offset="0" stop-color="var(--orange-light)"/>
        <stop offset="0.5" stop-color="var(--orange)"/>
        <stop offset="1" stop-color="var(--orange-deep)"/>
      </linearGradient>
    </defs>
    <text x="520" y="190" text-anchor="middle" font-size="208" textLength="1030" lengthAdjust="spacingAndGlyphs"
          fill="url(#headline-fill)" stroke="#1a0c04" stroke-width="6" paint-order="stroke">BRIDGING</text>
  </svg>

  <p class="tagline">Loan Service You Can<br>Rely On</p>

  <div class="advisor-figure" role="img" aria-label="3D illustration of a thoughtful business advisor in a blue suit"></div>

  <svg class="chat-bubble chat-bubble--bars" viewBox="0 0 350 200" aria-hidden="true">
    <defs>
      <linearGradient id="bubble-fill-a" x1="0" y1="0" x2="0" y2="1">
        <stop offset="0" stop-color="var(--bubble)"/>
        <stop offset="1" stop-color="var(--bubble-shade)"/>
      </linearGradient>
    </defs>
    <path d="M40 10 H300 Q330 10 330 40 V130 Q330 150 340 175 Q310 165 290 160 H40 Q10 160 10 130 V40 Q10 10 40 10 Z" fill="url(#bubble-fill-a)"/>
    <g fill="var(--icon)">
      <rect x="70" y="80" width="16" height="50" rx="8"/>
      <rect x="110" y="60" width="16" height="70" rx="8"/>
      <rect x="150" y="40" width="16" height="90" rx="8"/>
      <rect x="190" y="70" width="16" height="60" rx="8"/>
      <rect x="230" y="50" width="16" height="80" rx="8"/>
    </g>
  </svg>

  <svg class="chat-bubble chat-bubble--trend" viewBox="0 0 265 180" aria-hidden="true">
    <defs>
      <linearGradient id="bubble-fill-b" x1="0" y1="0" x2="0" y2="1">
        <stop offset="0" stop-color="var(--bubble)"/>
        <stop offset="1" stop-color="var(--bubble-shade)"/>
      </linearGradient>
    </defs>
    <path d="M40 10 H225 Q255 10 255 40 V115 Q255 145 225 145 H60 Q35 160 8 172 Q22 150 10 125 V40 Q10 10 40 10 Z" fill="url(#bubble-fill-b)"/>
    <g fill="none" stroke="var(--icon)" stroke-width="12" stroke-linecap="round" stroke-linejoin="round">
      <polyline points="60,90 105,55 140,80 195,40"/>
      <polyline points="170,40 195,40 195,65"/>
      <line x1="60" y1="118" x2="200" y2="118"/>
    </g>
  </svg>

  <svg class="offer-panel" viewBox="0 1940 1200 460" aria-hidden="true">
    <path d="M-10 2400 V2205 Q-10 2165 40 2155 L1090 1975 Q1160 1963 1185 2020 L1215 2090 V2400 Z"
          fill="var(--orange)" stroke="var(--white)" stroke-width="10"/>
  </svg>

  <p class="offer-text">5* Rated Service &amp;<br>No Broker Fees</p>
</main>
</body>
</html>
```